business card for a shoe shop

we would like a business card for a family owned shoe shop.
With this information included.
Darnell's Shoe Store
Family owned since 1947

then on other side
Darnell's Shoe Store
Footwear fitting specialist
Phone: 9187 2630
218 Quarry St, Fernleigh Downs 3187
(cnr. Hartwick Rd and Quarry St)
darnellshoes218@examplemail.com
if could incorporate the purple color on card i have attached.

```html
<!DOCTYPE html>
<html lang="en">
<head>
<meta charset="utf-8">
<title>Darnell's Shoe Store – Business Card</title>
<link href="https://fonts.googleapis.com/css2?family=Montserrat:wght@400;500&display=swap" rel="stylesheet">
<style>
  :root {
    --purple: #5e4b9e;
    --purple-deep: #4a3a86;
    --ink: #2a2a2e;
    --paper: #ffffff;
    --stage: #3a3a3c;
    --on-purple: #f4f1fb;
  }
  * { box-sizing: border-box; margin: 0; padding: 0; }
  html, body { width: 1200px; height: 1186px; overflow: hidden; }
  body {
    background: var(--stage);
    font-family: "Montserrat", sans-serif;
    position: relative;
  }
  .card {
    position: absolute;
    left: 250px;
    width: 700px;
    height: 400px;
    border-radius: 28px;
  }
  .card-front { top: 150px; background: var(--paper); color: var(--ink); }
  .card-back { top: 636px; background: var(--purple); color: var(--on-purple); }

  .brand-name {
    position: absolute;
    left: 48px;
    top: 150px;
    width: 260px;
    font-weight: 500;
    font-size: 34px;
    line-height: 1.15;
    color: var(--purple);
  }
  .divider {
    position: absolute;
    left: 330px;
    top: 110px;
    width: 2px;
    height: 150px;
    background: var(--purple);
  }
  .contact-list {
    position: absolute;
    left: 356px;
    top: 108px;
    list-style: none;
    font-size: 15px;
    line-height: 1.35;
  }
  .contact-list li { display: flex; align-items: center; gap: 10px; margin-bottom: 6px; }
  .contact-list svg { width: 14px; height: 14px; flex: none; fill: var(--purple); }
  .contact-address { margin-top: 12px; padding-left: 24px; display: block !important; }
  .tagline-front {
    position: absolute;
    right: 60px;
    bottom: 60px;
    font-size: 15px;
  }

  .back-name {
    position: absolute;
    left: 0; right: 0;
    top: 128px;
    text-align: center;
    font-weight: 500;
    font-size: 58px;
    color: var(--purple-deep);
  }
  .back-tagline {
    position: absolute;
    left: 0; right: 0;
    top: 250px;
    text-align: center;
    font-size: 20px;
    letter-spacing: 0.32em;
  }
</style>
</head>
<body>
  <section class="card card-front">
    <div class="brand-name">Darnell's Shoe Store</div>
    <div class="divider"></div>
    <ul class="contact-list">
      <li>
        <svg viewBox="0 0 24 24" aria-hidden="true"><path d="M6.6 10.8a15.1 15.1 0 0 0 6.6 6.6l2.2-2.2c.3-.3.7-.4 1-.2 1.1.4 2.3.6 3.6.6.6 0 1 .4 1 1V20c0 .6-.4 1-1 1A17 17 0 0 1 3 4c0-.6.4-1 1-1h3.5c.6 0 1 .4 1 1 0 1.3.2 2.5.6 3.6.1.3 0 .7-.2 1z"/></svg>
        9187 2630
      </li>
      <li>
        <svg viewBox="0 0 24 24" aria-hidden="true"><path d="M2 5h20v14H2zm2 2v.5l8 5 8-5V7l-8 5z"/></svg>
        darnellshoes218@examplemail.com
      </li>
      <li>
        <svg viewBox="0 0 24 24" aria-hidden="true"><path d="M12 2a10 10 0 1 0 0 20 10 10 0 0 0 0-20zm6.9 9h-3a15 15 0 0 0-1.3-6 8 8 0 0 1 4.3 6zM12 4c.9 1.3 1.7 3.9 1.9 7h-3.8C10.3 7.9 11.1 5.3 12 4zM9.4 5a15 15 0 0 0-1.3 6h-3a8 8 0 0 1 4.3-6zM5.1 13h3a15 15 0 0 0 1.3 6 8 8 0 0 1-4.3-6zm6.9 7c-.9-1.3-1.7-3.9-1.9-7h3.8c-.2 3.1-1 5.7-1.9 7zm2.6-1a15 15 0 0 0 1.3-6h3a8 8 0 0 1-4.3 6z"/></svg>
        www.darnellshoes.example
      </li>
      <li class="contact-address">
        218 Quarry St, Fernleigh Downs 3187<br>
        (cnr. Hartwick Rd and Quarry St)
      </li>
    </ul>
    <p class="tagline-front">Footwear fitting specialist</p>
  </section>

  <section class="card card-back">
    <div class="back-name">Darnell's Shoe Store</div>
    <p class="back-tagline">Family owned since 1947</p>
  </section>
</body>
</html>
```